Automotive Accessories Business Card

Design a business template that match our new logo design and our industry.

https://www.kelvramotive.com/

Target Market(s)

Aftermarket auto parts and accessories

Industry/Entity Type

automotive

Contact Information for Business Card

company logo

Font styles to use
Serif
Sans Serif

Colors
EB3D1F
EC4F4E
F09395
F8D3D4
FCEDEE

```html
<!DOCTYPE html>
<html lang="en">
<head>
<meta charset="utf-8">
<title>Kelvra Motive Inc – Business Card</title>
<link rel="stylesheet" href="https://fonts.googleapis.com/css2?family=Archivo:wght@800&display=swap">
<style>
  :root {
    --backdrop: #676767;
    --card-white: #fdfdfd;
    --brand-red: #d71f24;
    --charcoal: #414042;
  }
  html, body {
    margin: 0;
    padding: 0;
    width: 1200px;
    height: 1000px;
    overflow: hidden;
    background: var(--backdrop);
  }
  .canvas {
    position: relative;
    width: 1200px;
    height: 1000px;
  }
  .card-art {
    position: absolute;
    inset: 0;
  }
  .band-red { fill: var(--brand-red); }
  .band-dark { fill: var(--charcoal); }
  .card-face { fill: var(--card-white); }
  .brand {
    position: absolute;
    left: 0;
    width: 1200px;
    top: 462px;
    display: flex;
    justify-content: center;
    align-items: center;
    gap: 16px;
  }
  .brand-mark {
    width: 30px;
    height: 30px;
    background: var(--brand-red);
  }
  .brand-name {
    font-family: "Archivo", Arial, sans-serif;
    font-weight: 800;
    font-size: 50px;
    letter-spacing: 1px;
    line-height: 1;
    color: var(--charcoal);
    margin: 0;
    text-transform: uppercase;
  }
</style>
</head>
<body>
<main class="canvas">
  <svg class="card-art" width="1200" height="1000" viewBox="0 0 1200 1000" aria-hidden="true">
    <defs>
      <clipPath id="card-shape">
        <rect x="76" y="201" width="1048" height="597" rx="22" ry="22"/>
      </clipPath>
    </defs>
    <g clip-path="url(#card-shape)">
      <rect class="card-face" x="76" y="201" width="1048" height="597"/>
      <polygon class="band-dark" points="820,201 1124,201 1124,367 986,367"/>
      <polygon class="band-red" points="76,201 820,201 986,367 1124,367 1124,462 975,462 793,280 76,280"/>
      <polygon class="band-dark" points="76,585 210,585 423,798 76,798"/>
      <polygon class="band-red" points="76,507 258,507 443,692 1124,692 1124,798 423,798 210,585 76,585"/>
    </g>
  </svg>
  <div class="brand">
    <span class="brand-mark"></span>
    <h1 class="brand-name">Kelvra Motive Inc</h1>
  </div>
</main>
</body>
</html>
```